Web Instant Messenger Design Project

Hello,
The project consist of designing a web instant messenger interface. What we need is a Photoshop file that contains the design elements of this app. (windows, buttons , dropdowns etc)
notes:
- we are looking for the same look and feel as the now closed Tirvak.com
- the name of the app will be lurnbey.com , or similar.
- the application will be browser based, will cover 100% of the browser area.
- please don't make a "flat" background.
I attached 3 screen captures that shows the graphic elements we need :
img1: -
is the login "page" with username and password fields. There are also a connect & disconnect buttons + a register one
img2:
a) We have the classic friend list that shows who is online and their status. The friend list window can be moved and has 7
buttons (down:add friedn, delete friend, create group,change friend group and create conference / up: conference room list
and mass message buttons)
b) There is a conversation window that can be dragged. The conversation window will keep the private conversations and
conferences as a tab bar. Please note the key field area .
c) Mass Message window - here you can select the group and/or friends, write the message and hit send.
img3
a) on friend list window , when you click one of the down button a new , non movable window will appear. In this window you will have actions corresponding to the button you clicked : add/ delete friend , create conference , etc
b) public room window- is a drag-able window with the conferences you can join.
c)the conversation window with a conference selected. There is a invite buddy drop down, a list of participants and the conversations zone. On participants list there will be a kick and ban button.(not present in this capture)
Updates
When submitting a design please try to provide a mock of the "friend list window". Thank you and sorry if this info comes too late.
Industry/Entity Type
Group
Look and feel
Each slider illustrates characteristics of the customer's brand and the style your logo design should communicate.

```html
<!DOCTYPE html>
<html lang="en">
<head>
<meta charset="utf-8">
<title>lurnbey – Messenger</title>
<link rel="stylesheet" href="https://fonts.googleapis.com/css2?family=Cabin:wght@400;500;600;700&display=swap">
<style>
:root{
  --page-bg:#efefef;
  --header-top:#1788c9;
  --header-mid:#129ddc;
  --header-bot:#0d6fb0;
  --panel-bg:#ffffff;
  --panel-border:#cfcfcf;
  --line:#e1e1e1;
  --head-bg:#f7f7f7;
  --group-bg:#e4e4e4;
  --row-bg:#f9f9f9;
  --text:#333333;
  --muted:#888888;
  --btn-top:#4fb8d9;
  --btn-bot:#2794bb;
  --btn-border:#1f7fa3;
  --online:#6aa9c4;
  --offline:#c7c7c7;
  --self:#8c8c8c;
  --peer:#e0673a;
  --tip:#3a3a3a;
}
*{box-sizing:border-box;margin:0;padding:0}
html,body{width:1200px;height:700px;overflow:hidden}
body{position:relative;background:var(--page-bg) repeating-linear-gradient(45deg,rgba(0,0,0,.012) 0 2px,transparent 2px 4px);font-family:"Cabin",sans-serif;color:var(--text);font-size:14px}
.topbar{position:absolute;left:0;top:0;width:1200px;height:36px;background:linear-gradient(90deg,var(--header-bot),var(--header-mid) 50%,var(--header-bot));border-bottom:1px solid #0b5e96}
.brand{position:absolute;left:118px;top:2px;display:flex;align-items:center;gap:8px;color:#fff;font-weight:600;font-size:27px;line-height:30px}
.brand-mark{width:24px;height:24px;background:#fff;border-radius:3px}
.panel{position:absolute;top:50px;height:611px;background:var(--panel-bg);border:1px solid var(--panel-border)}
.friends{left:112px;width:250px}
.convs{left:372px;width:715px;background:#f4f4f4}
.panel-head{height:38px;border-bottom:1px solid var(--line);background:var(--head-bg);display:flex;align-items:center;gap:10px;padding-left:15px;font-weight:600;font-size:14px}
.convs .panel-head{padding-left:17px;gap:12px}
.btn{position:absolute;height:31px;border:1px solid var(--btn-border);border-radius:3px;background:linear-gradient(var(--btn-top),var(--btn-bot));color:#fff;font-family:inherit;font-weight:600;font-size:13px;text-align:left;padding-left:10px}
.status-label{position:absolute;left:63px;top:89px;font-size:13px}
.status-select{position:absolute;left:113px;top:85px;width:125px;height:23px;border:1px solid #d4d4d4;border-radius:2px;background:#fafafa;display:flex;align-items:center;padding-left:8px;gap:8px;font-size:13px}
.status-select .caret{position:absolute;right:0;top:0;width:26px;height:21px;border-left:1px solid #d4d4d4;display:flex;align-items:center;justify-content:center}
.list{position:absolute;left:0;top:118px;width:248px}
.group{height:29px;background:var(--group-bg);border-top:1px solid #d6d6d6;border-bottom:1px solid #d6d6d6;display:flex;justify-content:space-between;align-items:center;padding:0 16px 0 15px;font-weight:600;font-size:13px}
.friend{height:38px;background:var(--row-bg);border-bottom:1px solid var(--line);display:flex;align-items:center;padding:0 17px 0 23px;font-size:15px}
.friend:last-of-type{border-bottom:none}
.friend .name{flex:1}
.friend .state{font-style:italic;font-size:11px;color:var(--muted);margin-right:8px}
.toolbar{position:absolute;left:0;bottom:0;width:248px;height:33px;border-top:1px solid var(--line);display:flex;justify-content:space-around;align-items:center;padding:0 6px}
.tooltip{position:absolute;left:115px;top:658px;width:92px;height:25px;background:var(--tip);color:#fff;font-size:13px;line-height:25px;text-align:center}
.tabs{position:absolute;left:12px;top:46px;display:flex;gap:8px}
.tab{height:23px;border:1px solid #cfcfcf;border-radius:2px;background:#f7f7f7;display:flex;align-items:center;font-size:13px}
.tab .label{width:67px;text-align:center}
.tab .close{width:24px;height:21px;border-left:1px solid #cfcfcf;display:flex;align-items:center;justify-content:center;font-size:13px;font-weight:700;color:#777}
.section-bar{position:absolute;left:0;top:77px;width:713px;height:30px;background:#e2e2e2;border-top:1px solid #d2d2d2;border-bottom:1px solid #d2d2d2;padding-left:14px;line-height:28px;font-size:13px;font-weight:500}
.peer-name{position:absolute;left:14px;top:122px;font-size:14px}
.peer-state{position:absolute;left:14px;top:146px;font-size:14px}
.key-label{position:absolute;right:15px;top:119px;font-size:13px}
.field{position:absolute;background:#fff;border:1px solid #cccccc;border-radius:2px}
.key-field{left:488px;top:140px;width:213px;height:23px}
.chat{left:12px;top:170px;width:690px;height:388px;padding:10px 12px;font-size:14px;line-height:24px}
.chat .from-self{color:var(--self)}
.chat .from-peer{color:var(--peer)}
.compose{left:12px;top:566px;width:573px;height:31px}
.send{left:593px;top:566px;width:110px;text-align:center;padding-left:0}
</style>
</head>
<body>
<header class="topbar">
  <div class="brand"><span class="brand-mark"></span>lurnbey</div>
</header>

<section class="panel friends">
  <div class="panel-head">
    <svg width="22" height="16" viewBox="0 0 22 16"><g fill="#333"><circle cx="11" cy="4" r="3.5"/><path d="M4 16c0-5 3-7 7-7s7 2 7 7z"/><circle cx="4.5" cy="5.5" r="2.5"/><path d="M0 14c0-3 2-5 4.5-5 1 0 1.5.2 2 .5C5 11 4.5 12.5 4.5 14z"/><circle cx="17.5" cy="5.5" r="2.5"/><path d="M22 14c0-3-2-5-4.5-5-1 0-1.5.2-2 .5 1.5 1.5 2 3 2 4.5z"/></g></svg>
    Friend List
  </div>
  <button class="btn" style="left:8px;top:46px;width:110px">Mass Message</button>
  <button class="btn" style="left:129px;top:46px;width:110px">R.......</button>
  <span class="status-label">Starus</span>
  <div class="status-select">
    <svg width="18" height="14" viewBox="0 0 18 14"><path d="M1 1h10v7H5l-3 3V8H1z" fill="#7fb7cf"/><path d="M13 4h4v7h-1v3l-3-3H8V9h5z" fill="#a9cfdf"/></svg>
    Online
    <span class="caret"><svg width="8" height="5"><path d="M0 0h8L4 5z" fill="#888"/></svg></span>
  </div>

  <div class="list">
    <div class="group">Buddies<span>–</span></div>
    <div class="friend"><span class="name">Ionut</span><span class="state">Online</span><svg width="17" height="14" viewBox="0 0 17 14"><path d="M1 1h10v7H5l-3 3V8H1z" fill="var(--online)"/><path d="M12 4h4v7h-1v3l-3-3H7V9h5z" fill="var(--online)" opacity=".7"/></svg></div>
    <div class="friend"><span class="name">Admin</span><span class="state">Ofline</span><svg width="17" height="14" viewBox="0 0 17 14"><path d="M1 1h10v7H5l-3 3V8H1z" fill="var(--offline)"/><path d="M12 4h4v7h-1v3l-3-3H7V9h5z" fill="var(--offline)" opacity=".7"/></svg></div>
    <div class="friend"><span class="name">Cre1</span><span class="state">Ofline</span><svg width="17" height="14" viewBox="0 0 17 14"><path d="M1 1h10v7H5l-3 3V8H1z" fill="var(--offline)"/><path d="M12 4h4v7h-1v3l-3-3H7V9h5z" fill="var(--offline)" opacity=".7"/></svg></div>
    <div class="group">Kostel<span>–</span></div>
    <div class="friend"><span class="name">Big</span><span class="state">Ofline</span><svg width="17" height="14" viewBox="0 0 17 14"><path d="M1 1h10v7H5l-3 3V8H1z" fill="var(--offline)"/><path d="M12 4h4v7h-1v3l-3-3H7V9h5z" fill="var(--offline)" opacity=".7"/></svg></div>
    <div class="friend"><span class="name">Bigbig</span><span class="state">Online</span><svg width="17" height="14" viewBox="0 0 17 14"><path d="M1 1h10v7H5l-3 3V8H1z" fill="var(--online)"/><path d="M12 4h4v7h-1v3l-3-3H7V9h5z" fill="var(--online)" opacity=".7"/></svg></div>
    <div class="friend"><span class="name">Cre2</span><span class="state">Ofline</span><svg width="17" height="14" viewBox="0 0 17 14"><path d="M1 1h10v7H5l-3 3V8H1z" fill="var(--offline)"/><path d="M12 4h4v7h-1v3l-3-3H7V9h5z" fill="var(--offline)" opacity=".7"/></svg></div>
    <div class="group">Toba<span>–</span></div>
    <div class="friend"><span class="name">Bubu</span><span class="state">Online</span><svg width="17" height="14" viewBox="0 0 17 14"><path d="M1 1h10v7H5l-3 3V8H1z" fill="var(--online)"/><path d="M12 4h4v7h-1v3l-3-3H7V9h5z" fill="var(--online)" opacity=".7"/></svg></div>
    <div class="friend"><span class="name">Vasile</span><span class="state">Ofline</span><svg width="17" height="14" viewBox="0 0 17 14"><path d="M1 1h10v7H5l-3 3V8H1z" fill="var(--offline)"/><path d="M12 4h4v7h-1v3l-3-3H7V9h5z" fill="var(--offline)" opacity=".7"/></svg></div>
    <div class="friend"><span class="name">Crern12</span><span class="state">Ofline</span><svg width="17" height="14" viewBox="0 0 17 14"><path d="M1 1h10v7H5l-3 3V8H1z" fill="var(--offline)"/><path d="M12 4h4v7h-1v3l-3-3H7V9h5z" fill="var(--offline)" opacity=".7"/></svg></div>
    <div class="group">Work<span>+</span></div>
  </div>

  <div class="toolbar">
    <svg width="22" height="18" viewBox="0 0 22 18" aria-label="Add friend"><circle cx="7" cy="5" r="4" fill="#7cb342"/><path d="M0 18c0-6 3-8 7-8s7 2 7 8z" fill="#7cb342"/><path d="M15 11h2V9h2v2h2v2h-2v2h-2v-2h-2z" fill="#7cb342"/></svg>
    <svg width="24" height="18" viewBox="0 0 24 18" aria-label="Create group"><circle cx="6" cy="5" r="3.5" fill="#5b9fb5"/><circle cx="13" cy="5" r="3.5" fill="#5b9fb5"/><path d="M0 18c0-5 2.5-7 6-7s6 2 6 7z" fill="#5b9fb5"/><path d="M8 18c0-5 2-7 5-7s5 2 5 7z" fill="#5b9fb5"/><path d="M18 12h2v-2h2v2h2v2h-2v2h-2v-2h-2z" fill="#5b9fb5"/></svg>
    <svg width="22" height="18" viewBox="0 0 22 18" aria-label="Delete friend"><circle cx="7" cy="5" r="4" fill="#e06a3b"/><path d="M0 18c0-6 3-8 7-8s7 2 7 8z" fill="#e06a3b"/><rect x="14" y="13" width="7" height="2" fill="#e06a3b"/></svg>
    <svg width="24" height="18" viewBox="0 0 24 18" aria-label="Change friend group"><circle cx="6" cy="5" r="3.5" fill="#999"/><circle cx="12" cy="5" r="3.5" fill="#999"/><path d="M0 18c0-5 2.5-7 6-7s6 2 6 7z" fill="#999"/><path d="M7 18c0-5 2-7 5-7s5 2 5 7z" fill="#999"/><circle cx="19" cy="13" r="3.5" fill="none" stroke="#777" stroke-width="1.6"/></svg>
    <svg width="22" height="20" viewBox="0 0 22 20" aria-label="Create conference"><circle cx="11" cy="10" r="9" fill="none" stroke="#3a7ac9" stroke-width="1.5"/><circle cx="7" cy="8" r="3" fill="#e0673a"/><circle cx="15" cy="8" r="3" fill="#3a7ac9"/><path d="M2 18c0-4 2-6 5-6s5 2 5 6z" fill="#e0673a"/><path d="M10 18c0-4 2-6 5-6s5 2 5 6z" fill="#7cb342"/></svg>
  </div>
</section>
<div class="tooltip">Add Friedn</div>

<section class="panel convs">
  <div class="panel-head">
    <svg width="20" height="18" viewBox="0 0 20 18"><path d="M2 1h16a1 1 0 0 1 1 1v10a1 1 0 0 1-1 1H8l-5 4v-4H2a1 1 0 0 1-1-1V2a1 1 0 0 1 1-1z" fill="#333"/></svg>
    Your Conversations
  </div>
  <div class="tabs">
    <div class="tab"><span class="label">Ionut</span><span class="close">×</span></div>
    <div class="tab"><span class="label">Cre1</span><span class="close">×</span></div>
    <div class="tab"><span class="label">Cre2</span><span class="close">×</span></div>
    <div class="tab"><span class="label">Bubu</span><span class="close">×</span></div>
    <div class="tab"><span class="label" style="width:68px">vasile</span><span class="close">×</span></div>
    <div class="tab"><span class="label">Crerm12</span><span class="close">×</span></div>
  </div>
  <div class="section-bar">Personal Message</div>
  <div class="peer-name">Cre2</div>
  <div class="peer-state">Offiline</div>
  <div class="key-label">KeyCrypt(at least 4 characters)</div>
  <div class="field key-field"></div>
  <div class="field chat">
    <p><span class="from-self">Ionut:</span> hello</p>
    <p><span class="from-self">Ionut:</span> how are you doing</p>
    <p><span class="from-peer">Bubu:</span> hi</p>
    <p><span class="from-peer">Bubu:</span> I am fie :)</p>
  </div>
  <div class="field compose"></div>
  <button class="btn send">Send Message</button>
</section>
</body>
</html>
```